New Bicycle shop business card

Hi!
I'm looking for a business card for my new proffesional bike mechanics shop. This shop is only for fixing broken bikes and not selling bikes.
Peferbly a modern and sleek and modern design.
Colors: black, grey, red, white
Information:
Name: Velowerkplaats Martens
Shop owner: Bart Martens & Sofie Vanhulle
Website: www.velowerkplaats-martens.be
Email: info@velowerkplaats-martens.be
Phone number: +32471936208
Street adres: Molenweg 57
9470 Kreekdonk
Slogan/shop information: Herstellingen van alle merken.
Logo: see files.
Target Market(s)
People who seek a mechanic to fix or upgrade their bikes.
Contact Information for Business Card
Information:
Website: info@velowerkplaats-martens.be
9470 Kreekdonk
Logo: see files.

```html
<!DOCTYPE html>
<html lang="nl">
<head>
<meta charset="utf-8">
<title>Velowerkplaats Martens – visitekaartje</title>
<link rel="stylesheet" href="https://fonts.googleapis.com/css2?family=Montserrat:wght@600;700;800&family=Lato:wght@400;700;900&display=swap">
<style>
  :root {
    --ink: #1b1718;
    --red: #e0203a;
    --grey: #9a9a9a;
    --grey-line: #b9b9b9;
    --paper: #ffffff;
    --backdrop: #e6e9ea;
  }
  * { box-sizing: border-box; margin: 0; padding: 0; }
  html, body { width: 1200px; height: 900px; overflow: hidden; }
  body {
    background: var(--backdrop);
    font-family: "Lato", Arial, sans-serif;
    display: flex;
    flex-direction: column;
    align-items: center;
    justify-content: center;
    gap: 48px;
  }
  .card {
    width: 660px;
    height: 378px;
    position: relative;
    overflow: hidden;
    box-shadow: 0 10px 26px rgba(0,0,0,.16), 0 2px 4px rgba(0,0,0,.12);
  }

  /* Front */
  .card--front {
    background: var(--ink);
    display: flex;
    flex-direction: column;
    align-items: center;
    justify-content: center;
  }
  .brand {
    display: flex;
    flex-direction: column;
    align-items: center;
    gap: 18px;
  }
  .brand__dot { width: 64px; height: 64px; border-radius: 50%; background: var(--red); }
  .brand__name {
    font-family: "Montserrat", Arial, sans-serif;
    font-weight: 800;
    font-size: 38px;
    line-height: 1.1;
    letter-spacing: 3px;
    color: var(--paper);
    text-transform: uppercase;
    text-align: center;
  }
  .front__web {
    margin-top: 22px;
    font-size: 14px;
    letter-spacing: 1px;
    color: var(--grey);
    text-transform: uppercase;
  }

  /* Back */
  .card--back { background: var(--paper); }
  .slogan-band {
    position: absolute;
    left: 0; top: 40px;
    width: 480px; height: 64px;
    background: var(--ink);
    clip-path: polygon(0 0, 100% 0, 93% 100%, 0 100%);
    display: flex;
    align-items: center;
    padding-left: 36px;
  }
  .slogan-band__text {
    font-family: "Montserrat", Arial, sans-serif;
    font-weight: 700;
    font-size: 19px;
    letter-spacing: .4px;
    color: var(--paper);
    text-transform: uppercase;
  }
  .badge {
    position: absolute;
    left: 446px; top: 22px;
    width: 62px; height: 62px;
    border-radius: 50%;
    background: var(--red);
    border: 4px solid var(--paper);
  }
  .owners {
    position: absolute;
    left: 36px; top: 168px;
    right: 36px;
  }
  .owners__row { display: flex; align-items: flex-end; gap: 14px; }
  .owners__name {
    font-weight: 900;
    font-size: 27px;
    color: var(--ink);
    white-space: nowrap;
  }
  .owners__rule { flex: 1; height: 1px; background: var(--grey-line); margin-bottom: 9px; }
  .owners__role {
    margin-top: 4px;
    font-size: 13px;
    letter-spacing: .8px;
    color: var(--ink);
  }
  .contact {
    position: absolute;
    left: 36px; top: 256px;
    display: flex; flex-direction: column; gap: 8px;
  }
  .contact__line, .address {
    display: flex; align-items: flex-start; gap: 9px;
    font-size: 15px; color: var(--ink);
  }
  .icon { width: 14px; height: 14px; flex: none; margin-top: 2px; }
  .address {
    position: absolute;
    left: 400px; top: 256px;
    line-height: 1.35;
  }
</style>
</head>
<body>

<section class="card card--front" aria-label="Voorzijde visitekaartje">
  <div class="brand">
    <span class="brand__dot"></span>
    <span class="brand__name">Velowerkplaats<br>Martens</span>
  </div>
  <p class="front__web">www.velowerkplaats-martens.be</p>
</section>

<section class="card card--back" aria-label="Achterzijde visitekaartje">
  <div class="slogan-band"><span class="slogan-band__text">Herstellingen van alle merken</span></div>
  <span class="badge"></span>

  <div class="owners">
    <div class="owners__row">
      <span class="owners__name">Bart Martens &amp; Sofie Vanhulle</span>
      <span class="owners__rule"></span>
    </div>
    <p class="owners__role">SHOP OWNER</p>
  </div>

  <div class="contact">
    <p class="contact__line">
      <svg class="icon" viewBox="0 0 14 14" aria-hidden="true"><rect x="0.5" y="2.5" width="13" height="9" fill="#e0203a"/><path d="M1 3 L7 8 L13 3" fill="none" stroke="#fff" stroke-width="1.3"/></svg>
      info@velowerkplaats-martens.be
    </p>
    <p class="contact__line">
      <svg class="icon" viewBox="0 0 14 14" aria-hidden="true"><path d="M3 1.5 L5 1.5 L6 4.5 L4.5 5.8 C5.3 7.6 6.4 8.7 8.2 9.5 L9.5 8 L12.5 9 L12.5 11 C12.5 12 11.6 12.7 10.6 12.5 C5.9 11.6 2.4 8.1 1.5 3.4 C1.3 2.4 2 1.5 3 1.5 Z" fill="#e0203a"/></svg>
      +32471936208
    </p>
  </div>

  <p class="address">
    <svg class="icon" viewBox="0 0 14 14" aria-hidden="true"><path d="M7 13.5 C7 13.5 2 8.3 2 5.2 A5 5 0 0 1 12 5.2 C12 8.3 7 13.5 7 13.5 Z" fill="#e0203a"/><circle cx="7" cy="5.2" r="1.9" fill="#fff"/></svg>
    <span>Molenweg 57<br>9470 Kreekdonk</span>
  </p>
</section>

</body>
</html>
```